Graphic Design for a 3 Banner Tradeshow Setup

We are a Pipe Restoration company that specializes in trenchless pipelining. We need a design for a 3 banner setup to use at tradeshows. See attached "banner specs" for sizing - note the 48" x 92" will be in between the two 36" x 92" banners. See attached "Mock-Up" of information each banner needs and utilize the color scheme of the banners we already have in the "both MLD banners" AI file attached. The final designs should communicate what we do and attract people into our booth. We would like to have graphics of realistic pipes for a before (dirty pipe), after cleaning pipe, and lined pipe - see example of "pipe pictures" attached. I'm not sure if this is something you can generate or if we will need to find images of our own to send. Also, see attached "screenshot-process" to see similar images we would like to use to showcase the process.
Target Market(s)
Homeowners, Property Managers, HOA Communities, Healthcare Facilities & Hospitals, and commercial properties
Industry/Entity Type
Trenchless Pipelining
Look and feel
Each slider illustrates characteristics of the customer's brand and the style your logo design should communicate.

```html
<!DOCTYPE html>
<html lang="en">
<head>
<meta charset="utf-8">
<title>MLD Tradeshow Banners</title>
<link href="https://fonts.googleapis.com/css2?family=Oswald:wght@500;700&family=Share+Tech&display=swap" rel="stylesheet">
<style>
  :root{
    --bg:#cdeefb;
    --navy:#153a73;
    --navy-deep:#0f2c5c;
    --blue:#1c64b8;
    --blue-mid:#2474c9;
    --accent:#3b8ee0;
    --white:#ffffff;
    --strip:#f2f4f7;
    --rust:#6b3d22;
    --steel:#b9b3a8;
    --liner:#6fc6e6;
    --marker:#1a4f9a;
  }
  *{box-sizing:border-box;margin:0;padding:0}
  html,body{width:1200px;height:957px;overflow:hidden;background:var(--bg)}
  .stage{position:relative;width:1200px;height:957px}
  .banner{position:absolute;top:60px;height:840px;overflow:hidden;
    background:linear-gradient(180deg,var(--blue) 0%,var(--blue-mid) 55%,var(--blue) 100%);color:var(--white)}
  .banner--left{left:70px;width:320px}
  .banner--center{left:430px;width:380px}
  .banner--right{left:850px;width:320px}
  .banner__head{position:absolute;left:0;top:0;width:100%;height:150px;background:var(--navy);
    border-bottom:6px solid var(--accent)}
  .brand{position:absolute;left:0;right:0;top:40px;text-align:center}
  .brand__row{display:inline-flex;align-items:center;gap:10px}
  .brand__mark{width:30px;height:30px;background:var(--white)}
  .brand__name{font-family:'Oswald',sans-serif;font-weight:700;font-size:54px;line-height:1;color:var(--white);letter-spacing:4px}
  .brand__sub{display:block;margin-top:6px;font-family:'Oswald',sans-serif;font-weight:500;font-size:11px;letter-spacing:2.5px;color:var(--white)}
  .photo{position:absolute}
  .heading{position:absolute;font-family:'Oswald',sans-serif;font-weight:700;line-height:1.02;color:var(--white)}
  .list{position:absolute;list-style:none;font-family:'Share Tech',sans-serif;color:var(--white)}
  .list li{display:flex;align-items:center;gap:10px}
  .list li::before{content:"";flex:none;width:0;height:0;border-top:7px solid transparent;border-bottom:7px solid transparent;border-left:9px solid var(--white)}
  .deco{position:absolute}

  /* left banner */
  .assess__photo{left:0;top:180px;width:320px;height:250px;
    background:linear-gradient(90deg,var(--rust) 0%,#8a5a3a 45%,var(--steel) 55%,#ddd8cf 100%)}
  .assess__title{left:26px;top:470px;font-size:44px}
  .assess__list{left:26px;top:532px;font-size:23px}
  .assess__list li{margin-bottom:8px}
  .contact{position:absolute;left:0;top:690px;width:100%;height:150px;background:var(--navy-deep);text-align:center;padding-top:18px}
  .contact__line{font-family:'Share Tech',sans-serif;font-size:24px;line-height:1.2}
  .social{display:flex;justify-content:center;gap:22px;margin-top:16px}
  .social span{width:38px;height:38px;border-radius:50%;background:var(--white)}

  /* center banner */
  .problems__title{left:34px;top:188px;font-size:58px}
  .problems__text{position:absolute;left:34px;top:330px;width:330px;font-family:'Share Tech',sans-serif;font-size:25px;line-height:1.45;letter-spacing:.5px}
  .problems__photo{left:30px;top:470px;width:320px;height:160px;border-radius:80px;
    background:linear-gradient(90deg,var(--rust) 0%,#8a5a3a 50%,var(--liner) 70%,#bfe8f6 100%)}
  .process{position:absolute;left:0;top:655px;width:100%;height:65px;background:var(--strip);display:flex;gap:14px;padding:12px 20px}
  .process span{flex:1;height:38px}
  .process .step-1{background:linear-gradient(90deg,#2b2f33,#4a5a4e)}
  .process .step-2{background:linear-gradient(90deg,#1d1f22,var(--liner),#1d1f22)}
  .process .step-3{background:linear-gradient(90deg,var(--liner),#9fdcf2)}
  .center-foot{position:absolute;left:0;top:720px;width:100%;height:120px;background:var(--navy)}

  /* right banner */
  .fix__title{left:34px;top:190px;font-size:68px}
  .fix__list{left:20px;top:290px;font-size:25px}
  .fix__list li{margin-bottom:12px;align-items:flex-start}
  .fix__list li::before{margin-top:8px}
  .fix__photo{left:90px;top:590px;width:230px;height:250px;
    background:radial-gradient(ellipse at 50% 60%,#25366e 0%,#1b2a58 60%,rgba(27,42,88,0) 75%)}
</style>
</head>
<body>
<div class="stage">

  <section class="banner banner--left">
    <header class="banner__head">
      <div class="brand"><span class="brand__row"><span class="brand__mark"></span><span class="brand__name">MLD</span></span><span class="brand__sub">MAIN LINE DRAIN SOLUTIONS</span></div>
    </header>
    <div class="photo assess__photo" role="img" aria-label="Photo of a corroded pipe beside a restored clean pipe"></div>
    <svg class="deco" style="left:240px;top:440px" width="70" height="20" viewBox="0 0 70 20"><path d="M16 2 L4 10 L16 18Z" fill="#fff"/><path d="M50 2 L38 10 L50 18" fill="none" stroke="#fff" stroke-width="2"/></svg>
    <h2 class="heading assess__title">WE ASSESS</h2>
    <ul class="list assess__list">
      <li>CCTV Pipe Investigation</li>
      <li>Scope Development</li>
      <li>Budgetary Evaluation</li>
      <li>Project Oversight</li>
    </ul>
    <footer class="contact">
      <p class="contact__line">info@mainlinedrain.com</p>
      <p class="contact__line">+00 555-010-2040</p>
      <div class="social" aria-label="Social channels"><span></span><span></span><span></span></div>
    </footer>
  </section>

  <section class="banner banner--center">
    <header class="banner__head">
      <div class="brand"><span class="brand__row"><span class="brand__mark"></span><span class="brand__name">MLD</span></span><span class="brand__sub">MAIN LINE DRAIN SOLUTIONS</span></div>
    </header>
    <svg class="deco" style="left:290px;top:165px" width="80" height="125" viewBox="0 0 80 125">
      <g fill="none" stroke="#fff" stroke-width="2.5"><path d="M4 6 L18 16 L32 6"/><path d="M4 22 L18 32 L32 22"/><path d="M4 38 L18 48 L32 38"/></g>
      <g stroke="#fff" stroke-width="1.5"><path d="M62 2 L74 14 L62 26 L50 14Z" fill="none"/><path d="M62 30 L74 42 L62 54 L50 42Z" fill="var(--marker)" stroke="none"/><path d="M62 58 L74 70 L62 82 L50 70Z" fill="none"/><path d="M62 86 L74 98 L62 110 L50 98Z" fill="none"/></g>
    </svg>
    <h1 class="heading problems__title">PIPE<br>PROBLEMS?</h1>
    <p class="problems__text">WE HELP FIX PIPE PROBLEMS WITHOUT HAVING TO TEAR UP YOUR BUILDING</p>
    <div class="photo problems__photo" role="img" aria-label="Photo of a rusted pipe section next to a lined blue pipe"></div>
    <div class="process" role="img" aria-label="Three photos of the pipelining process steps"><span class="step-1"></span><span class="step-2"></span><span class="step-3"></span></div>
    <div class="center-foot"></div>
  </section>

  <section class="banner banner--right">
    <header class="banner__head">
      <div class="brand"><span class="brand__row"><span class="brand__mark"></span><span class="brand__name">MLD</span></span><span class="brand__sub">MAIN LINE DRAIN SOLUTIONS</span></div>
    </header>
    <svg class="deco" style="left:280px;top:175px" width="28" height="130" viewBox="0 0 28 130">
      <g stroke="#fff" stroke-width="2"><path d="M2 4 H26 L14 18Z" fill="var(--marker)" stroke="none"/><path d="M2 26 H26 L14 42Z" fill="none"/><path d="M2 50 H26 L14 64Z" fill="var(--marker)" stroke="none"/><path d="M2 72 H26 L14 88Z" fill="none"/><path d="M2 96 H26 L14 110Z" fill="var(--marker)" stroke="none"/><path d="M2 112 H26 L14 128Z" fill="none"/></g>
    </svg>
    <h2 class="heading fix__title">We Fix</h2>
    <ul class="list fix__list">
      <li>Slow Drains</li>
      <li>Back-Ups</li>
      <li>Sewer Odors</li>
      <li>Cracked Pipes</li>
      <li>Root Intrusion</li>
      <li>Recurring Plumbing<br>Problems</li>
    </ul>
    <div class="photo fix__photo" role="img" aria-label="Photo of a smiling plumber in navy overalls holding a pipe wrench"></div>
  </section>

</div>
</body>
</html>
```